DESKHAVEN COWORKING Website design and coding

DESKHAVEN COWORKING

DESKHAVEN is Galveston’s first (and currently only) shared business co-working space. We share the same upscale, casual work environment, but we work independently on our own (or our team’s) projects and goals. For only a flat $195 membership fee per month, you have your very own all-inclusive, fun, personal business office environment. Website is written (Word file #12, below); and all pictures etc provided. Galveston is a beachy, coastal, historic city an hour from Houston, Texas USA. Logo (file 11 below) is temporary only.

Target Market(s)

Outside sales people, medical students looking for study hall, Houston companies looking for local office, real estate agents, graphic artists, entrepreneurs, etc

Contact Information for Business Card

will discuss --want to combine with current business card with multiple businesses

Logo Text

DESKHAVEN COWORKING

Coding

Coded - Design and coding required

Number of Pages Required

5+ page

Colors
ec1f27
fbed22

Requirements
Nice to have
• maroon/wine dominant with yellow and red accents, gray base are the colors of the space--website could coordinate--but open to creative ideas/combinations

```html
<!DOCTYPE html>
<html lang="en">
<head>
<meta charset="utf-8">
<title>DESKHAVEN Coworking</title>
<link rel="stylesheet" href="https://fonts.googleapis.com/css2?family=Roboto:wght@300;400;500;700&display=swap">
<style>
  :root {
    --brand-red: #ec1f27;
    --brand-yellow: #fbed22;
    --ink: #111111;
    --text-dark: #222222;
    --border: #d9d9d9;
    --white: #ffffff;
    --shade: rgba(20, 14, 10, 0.55);
  }
  * { box-sizing: border-box; margin: 0; padding: 0; }
  html, body { width: 1200px; height: 574px; overflow: hidden; background: var(--white); }
  body { font-family: "Roboto", Arial, sans-serif; color: var(--text-dark); position: relative; }

  .site-header { position: absolute; top: 0; left: 0; width: 1200px; height: 90px; border-top: 1px solid var(--border); }
  .brand { position: absolute; left: 147px; top: 24px; color: var(--brand-red); font-weight: 700; line-height: 1; }
  .brand-name { display: block; font-size: 29px; letter-spacing: 0.5px; }
  .brand-sub { display: block; font-size: 15px; letter-spacing: 4.2px; margin-top: 3px; padding-left: 2px; }

  .search { position: absolute; left: 374px; top: 31px; width: 448px; height: 29px; display: flex; }
  .search-input { flex: 1; border: 1px solid var(--border); border-right: none; border-radius: 3px 0 0 3px; font: 400 12px "Roboto", Arial, sans-serif; color: #777; padding: 0 9px; display: flex; align-items: center; }
  .search-category { width: 104px; border: 1px solid var(--border); font-size: 11px; color: var(--text-dark); display: flex; align-items: center; justify-content: center; gap: 8px; }
  .search-button { width: 35px; background: var(--ink); border-radius: 0 3px 3px 0; display: flex; align-items: center; justify-content: center; }

  .account-links { position: absolute; top: 29px; left: 970px; display: flex; gap: 14px; }
  .account-link { display: flex; flex-direction: column; align-items: center; font-size: 9px; color: var(--text-dark); width: 36px; gap: 3px; }

  .main-nav { position: absolute; top: 90px; left: 0; width: 1200px; height: 29px; background: var(--brand-yellow); }
  .main-nav ul { list-style: none; display: flex; height: 100%; padding-left: 134px; }
  .main-nav li { display: flex; align-items: center; padding: 0 10px; font-size: 12px; font-weight: 500; color: var(--brand-red); border-left: 1px solid rgba(0,0,0,0.06); }
  .main-nav li:first-child { border-left: none; }

  .hero { position: absolute; top: 127px; left: 0; width: 1200px; height: 447px; }
  .hero-photo { position: absolute; inset: 0;
    background:
      radial-gradient(ellipse at 80% 35%, rgba(236, 220, 150, 0.85), transparent 45%),
      linear-gradient(90deg, #6e7478 0%, #8e9296 22%, #4b2e2a 40%, #5a1f25 62%, #b59a6a 85%, #d9cfa5 100%);
  }
  .hero-photo::after { content: ""; position: absolute; left: 0; right: 0; bottom: 0; height: 45%; background: linear-gradient(180deg, transparent, rgba(35, 22, 18, 0.75)); }
  .hero-content { position: absolute; left: 188px; top: 179px; color: var(--white); }
  .hero-title { font-weight: 400; font-size: 36px; line-height: 39px; }
  .hero-title span { background: var(--shade); padding: 0 1px; }
  .hero-tagline { margin-top: 12px; font-weight: 300; font-size: 19px; }
  .hero-tagline span { background: var(--shade); }
  .hero-cta { margin-top: 23px; width: 164px; height: 40px; border: 1.5px solid var(--white); border-radius: 3px; display: flex; align-items: center; justify-content: center; gap: 10px; font-weight: 700; font-size: 18px; background: rgba(0,0,0,0.25); }
</style>
</head>
<body>
  <header class="site-header">
    <div class="brand">
      <span class="brand-name">DESKHAVEN</span>
      <span class="brand-sub">coworking</span>
    </div>
    <div class="search">
      <div class="search-input">Search</div>
      <div class="search-category">All categories
        <svg width="8" height="5" viewBox="0 0 8 5"><path d="M1 1l3 3 3-3" fill="none" stroke="#888" stroke-width="1"/></svg>
      </div>
      <div class="search-button">
        <svg width="11" height="11" viewBox="0 0 12 12"><circle cx="5" cy="5" r="3.8" fill="none" stroke="#fff" stroke-width="1.3"/><path d="M8 8l3 3" stroke="#fff" stroke-width="1.3"/></svg>
      </div>
    </div>
    <nav class="account-links">
      <div class="account-link">
        <svg width="18" height="18" viewBox="0 0 18 18"><circle cx="9" cy="5.5" r="4" fill="none" stroke="#222" stroke-width="1.3"/><path d="M1.5 17c0-4 3.4-6 7.5-6s7.5 2 7.5 6z" fill="none" stroke="#222" stroke-width="1.3"/></svg>
        Login
      </div>
      <div class="account-link">
        <svg width="19" height="17" viewBox="0 0 20 18"><path d="M10 16.5S1.5 11 1.5 5.5A4 4 0 0 1 10 3.5a4 4 0 0 1 8.5 2C18.5 11 10 16.5 10 16.5z" fill="none" stroke="#222" stroke-width="1.3"/></svg>
        Wishlist
      </div>
    </nav>
  </header>

  <nav class="main-nav">
    <ul>
      <li>ABOUT</li>
      <li>MEMBERSHIP</li>
      <li>THE DESKHAVEN PHILOSOPHY</li>
      <li>PICTURES</li>
      <li>AMENITIES</li>
      <li>CONTACT</li>
    </ul>
  </nav>

  <section class="hero">
    <div class="hero-photo" role="img" aria-label="Photo of the coworking kitchen with steel fridge, wine-red bar counter and wooden stools"></div>
    <div class="hero-content">
      <h1 class="hero-title"><span>Discover the Best shared</span><br><span>Business Co-Working Space</span></h1>
      <p class="hero-tagline"><span>The most upscale, casual work environment!</span></p>
      <div class="hero-cta">Click Here
        <svg width="20" height="10" viewBox="0 0 20 10"><path d="M0 5h18M14 1l4 4-4 4" fill="none" stroke="#fff" stroke-width="2"/></svg>
      </div>
    </div>
  </section>
</body>
</html>
```